Invest in Real Estate housing and apartment development projects in Lima - Peru

Need a presentation for Grupo Venora, a top Real Estate developer from Peru who is looking for new leading investors such as Top Regional and Worldwide Real Estate funds and Regional Family offices and High Networth individuals to invest in Real Estate projects developed by/with Grupo Venora. Venora is focused on middle income apartments (housing) and has developed and delivered aprox 1400 apartments, and is currently developing and building 400 apartments. Venora currently has a potential to develop 1500 more apartments. And is looking to raise between US $50 and 60mm dollars a year in additional new investments, all focused on real estate housing (essentially vertical housing, apartments)
I have already some information and slides prepared with information regarding management fees, development and sales/marketing fees, success fees which are alligned to IRR of the project.

Target Market(s)

Real Estate investors in Latin America

Industry/Entity Type

Real Estate Development

Colors

Requirements
Must have
• Graphs and pictures of real estate projects. Data of housing market from Lima, capital of Peru compared to other top capitals in South America

```html
<!DOCTYPE html>
<html lang="es">
<head>
<meta charset="utf-8">
<title>Grupo Venora – Presentación a inversionistas</title>
<link href="https://fonts.googleapis.com/css2?family=Cabin:wght@400;500;600&display=swap" rel="stylesheet">
<style>
:root{
  --green:#6cbf3f;
  --green-dark:#1f9a45;
  --green-light:#8dc63f;
  --lime:#d6df23;
  --teal:#1aa88a;
  --slate:#3d4446;
  --text:#333a3c;
  --muted:#8a8f91;
  --page:#ececea;
  --white:#ffffff;
}
*{margin:0;padding:0;box-sizing:border-box}
html,body{width:1200px;height:900px;overflow:hidden}
body{background:var(--page);font-family:"Cabin",sans-serif;color:var(--text);position:relative}
.slide{position:absolute;width:368px;height:276px;background:var(--white);box-shadow:0 10px 18px rgba(0,0,0,.18)}
.slide__frame{position:absolute;inset:8px;border:1.5px solid var(--green)}
.slide__title{position:absolute;left:0;right:0;text-align:center;color:var(--green);font-weight:500;font-size:17px;line-height:1.22}
.page-num{position:absolute;right:14px;bottom:12px;width:17px;height:17px;border-radius:50%;background:var(--green);color:var(--white);font-size:10px;text-align:center;line-height:17px}
.slide svg{position:absolute;left:0;top:0}

/* Cover */
.cover{left:26px;top:146px}
.cover__photo{position:absolute}
.cover__brand{position:absolute;left:94px;top:98px;width:178px;height:60px;background:var(--white);border:1.5px solid var(--green);display:flex;align-items:center;gap:8px;padding-left:12px}
.cover__mark{width:26px;height:26px;border-radius:50%;background:var(--green);flex:none}
.cover__name{font-size:25px;font-weight:600;color:var(--slate);letter-spacing:.5px}
.cover__footer{position:absolute;left:0;right:0;bottom:0;height:14px;background:rgba(255,255,255,.92);font-size:5.6px;color:var(--slate);line-height:14px;padding-left:20px}
.cover__social{position:absolute;bottom:20px;width:11px;height:11px;border-radius:50%;background:var(--green)}

/* Strategic asset */
.strategic{left:424px;top:146px}
.pillar{position:absolute;top:56px;width:108px;text-align:center}
.pillar__label{font-size:7px;font-weight:600;margin-top:4px}
.bullets{list-style:none;position:absolute;font-size:5.4px;line-height:1.3}
.bullets li{position:relative;padding-left:9px;margin-bottom:6px}
.bullets li::before{content:"";position:absolute;left:0;top:1px;width:5.5px;height:5.5px;border-radius:50%;background:var(--green)}
.footnote{position:absolute;left:27px;bottom:10px;font-size:5.6px}

/* Chart slide */
.portfolio{left:818px;top:146px}

/* Peru */
.peru{left:213px;top:478px}
.peru h3{position:absolute;font-weight:500;font-size:10px;color:var(--text);line-height:1.25}
.country{position:absolute;font-size:6px;line-height:1.3}
.country b{font-weight:600}
.country--peru{color:var(--green)}
.flag{position:absolute;width:13px;height:8px;display:flex}
.flag span{flex:1}
.flag--h{flex-direction:column}
.peru .bullets{font-size:7.2px;line-height:1.3}
.peru .bullets li{padding-left:12px;margin-bottom:9px}
.peru .bullets li::before{width:6px;height:6px;top:2px}

/* Companies */
.companies{left:603px;top:478px}
.note{position:absolute;font-size:5.8px;line-height:1.25;color:var(--muted)}
</style>
</head>
<body>

<!-- Slide 1: cover -->
<section class="slide cover">
  <div class="cover__photo" role="img" aria-label="Render de edificios de departamentos con zona de juegos infantiles" style="left:0;top:0;width:120px;height:100px;background:linear-gradient(160deg,#b9a58a,#8fa36a 70%,#6f9b3c)"></div>
  <div class="cover__photo" role="img" aria-label="Render de terraza con piscina y palmeras frente a cerros" style="left:120px;top:0;width:144px;height:100px;background:linear-gradient(180deg,#c9d6e6,#8a8b7a 45%,#6aa1c9 75%,#79a85a)"></div>
  <div class="cover__photo" role="img" aria-label="Render de torres residenciales altas" style="left:264px;top:0;width:104px;height:100px;background:linear-gradient(180deg,#d9dde0,#a9aeb3 55%,#7f9a5c)"></div>
  <div class="cover__photo" role="img" aria-label="Render de bloques de departamentos con juegos infantiles" style="left:0;top:100px;width:120px;height:100px;background:linear-gradient(170deg,#dfe3e6,#b3b6b9 50%,#8eae5c)"></div>
  <div class="cover__photo" role="img" aria-label="Render de jardín en azotea con vegetación" style="left:264px;top:100px;width:104px;height:70px;background:linear-gradient(160deg,#8c7b6c,#6e9a45 60%,#4f7d2e)"></div>
  <div class="cover__photo" role="img" aria-label="Render de piscina rodeada de edificios" style="left:0;top:200px;width:120px;height:76px;background:linear-gradient(180deg,#c08e7c,#7fa8c8 55%,#3f8fc9)"></div>
  <div class="cover__photo" role="img" aria-label="Render de edificios de ladrillo con áreas verdes" style="left:120px;top:158px;width:110px;height:118px;background:linear-gradient(170deg,#cfd7de,#a57e62 50%,#7ea652)"></div>
  <div class="cover__photo" role="img" aria-label="Render de terraza con sombrillas y sala exterior frente al mar" style="left:230px;top:155px;width:138px;height:121px;background:linear-gradient(180deg,#d8dee3,#9fb7c4 40%,#e9ecee 65%,#6d6f70)"></div>
  <div class="cover__brand">
    <span class="cover__mark"></span>
    <span class="cover__name">Grupo Venora</span>
  </div>
  <span class="cover__social" style="left:323px"></span>
  <span class="cover__social" style="left:338px"></span>
  <div class="cover__footer">www.grupovenora.com.pe | Telephone Central: 410 2200 | contact@grupovenora.com.pe | Grupo Venora © 2016 - All rights reserved</div>
</section>

<!-- Slide 2: strategic asset -->
<section class="slide strategic">
  <div class="slide__frame"></div>
  <h2 class="slide__title" style="top:19px">Real Estate Como Asset Estratégico</h2>

  <div class="pillar" style="left:18px">
    <svg width="108" height="66" viewBox="0 0 108 66" style="position:static">
      <polygon points="54,2 84,19 84,49 54,66 24,49 24,19" fill="var(--green)"/>
      <g stroke="#fff" stroke-width="1.6" fill="none">
        <circle cx="54" cy="34" r="6"/>
        <circle cx="54" cy="19" r="3"/><circle cx="54" cy="49" r="3"/>
        <circle cx="40" cy="27" r="3"/><circle cx="68" cy="27" r="3"/>
        <circle cx="40" cy="41" r="3"/><circle cx="68" cy="41" r="3"/>
        <path d="M54 22v6M54 40v6M43 28.5l6 3M65 28.5l-6 3M43 39.5l6-3M65 39.5l-6-3"/>
      </g>
    </svg>
    <div class="pillar__label">Diversificación</div>
  </div>
  <div class="pillar" style="left:132px">
    <svg width="108" height="66" viewBox="0 0 108 66" style="position:static">
      <polygon points="54,2 84,19 84,49 54,66 24,49 24,19" fill="var(--green-dark)"/>
      <g fill="#fff">
        <rect x="40" y="36" width="4" height="12"/><rect x="46" y="31" width="4" height="17"/><rect x="52" y="26" width="4" height="22"/>
        <path d="M63 30c4 6 7 9 7 13a7 7 0 0 1-14 0c0-4 3-7 7-13z"/>
      </g>
      <path d="M38 32l12-12" stroke="#fff" stroke-width="2"/><path d="M45 19h6v6" stroke="#fff" stroke-width="2" fill="none"/>
      <text x="63" y="47" fill="var(--green-dark)" font-size="9" font-weight="600" text-anchor="middle" font-family="Cabin, sans-serif">$</text>
    </svg>
    <div class="pillar__label">Generación de valor</div>
  </div>
  <div class="pillar" style="left:246px">
    <svg width="108" height="66" viewBox="0 0 108 66" style="position:static">
      <polygon points="54,2 84,19 84,49 54,66 24,49 24,19" fill="var(--lime)"/>
      <path d="M48 16h12v18h9L54 52 39 34h9z" fill="#fff"/>
    </svg>
    <div class="pillar__label">Downside limitado</div>
  </div>

  <ul class="bullets" style="left:24px;top:145px;width:105px">
    <li>Baja correlación con mercados financieros y activos tradicionales: bonos, acciones; etc.</li>
    <li>HNWI a nivel global destinan el 17.9% de su portafolio a real estate vs. el 21.9% en Latinoamérica 1/</li>
  </ul>
  <ul class="bullets" style="left:139px;top:145px;width:105px">
    <li>Retorno potencial alto y estable: TIR alrededor de 12-15%</li>
    <li>Tickets de inversión moldeables</li>
    <li>Posibilidad de mayores retornos ante aumento de apalancamiento</li>
  </ul>
  <ul class="bullets" style="left:253px;top:145px;width:92px">
    <li>Acotado al valor del inmueble o terreno</li>
  </ul>

  <p class="footnote">1/ HNWI: High Net Worth Individuals según Global Wealth Review 2016</p>
  <span class="page-num">2</span>
</section>

<!-- Slide 3: portfolio chart -->
<section class="slide portfolio">
  <div class="slide__frame"></div>
  <h2 class="slide__title" style="top:10px">Real Estate : componente esencial en<br>cualquier portafolio diversificado</h2>
  <svg width="368" height="276" viewBox="0 0 368 276" font-family="Cabin, sans-serif">
    <g stroke="#e3e5e6" stroke-width=".6">
      <line x1="80" y1="108" x2="300" y2="108"/><line x1="80" y1="122" x2="300" y2="122"/>
      <line x1="80" y1="136" x2="300" y2="136"/><line x1="80" y1="150" x2="300" y2="150"/>
      <line x1="80" y1="164" x2="300" y2="164"/><line x1="80" y1="178" x2="300" y2="178"/>
      <line x1="80" y1="193" x2="300" y2="193"/><line x1="80" y1="207" x2="300" y2="207"/>
      <line x1="80" y1="221" x2="300" y2="221"/>
    </g>
    <line x1="80" y1="235" x2="300" y2="235" stroke="#b8bcbe" stroke-width=".8"/>
    <g font-size="6.5" fill="var(--muted)" text-anchor="end">
      <text x="74" y="110">90</text><text x="74" y="124">80</text><text x="74" y="138">70</text>
      <text x="74" y="152">60</text><text x="74" y="166">50</text><text x="74" y="180">40</text>
      <text x="74" y="195">30</text><text x="74" y="209">20</text><text x="74" y="223">10</text>
    </g>
    <!-- bars: top segment then base -->
    <g>
      <rect x="90" y="179" width="9" height="21" fill="var(--green-light)"/><rect x="90" y="200" width="9" height="35" fill="var(--slate)"/>
      <rect x="110" y="164" width="9" height="15" fill="var(--green)"/><rect x="110" y="179" width="9" height="56" fill="var(--slate)"/>
      <rect x="143" y="108" width="9" height="50" fill="var(--green-dark)"/><rect x="143" y="158" width="9" height="77" fill="var(--slate)"/>
      <rect x="163" y="136" width="9" height="28" fill="var(--lime)"/><rect x="163" y="164" width="9" height="71" fill="var(--slate)"/>
      <rect x="197" y="150" width="9" height="40" fill="var(--green-light)"/><rect x="197" y="190" width="9" height="45" fill="var(--slate)"/>
      <rect x="217" y="122" width="9" height="61" fill="var(--lime)"/><rect x="217" y="183" width="9" height="52" fill="var(--slate)"/>
      <rect x="250" y="136" width="9" height="42" fill="var(--green-light)"/><rect x="250" y="178" width="9" height="57" fill="var(--slate)"/>
      <rect x="270" y="122" width="9" height="68" fill="var(--green-dark)"/><rect x="270" y="190" width="9" height="45" fill="var(--slate)"/>
    </g>
    <!-- markers -->
    <g font-size="5.5" fill="#fff" text-anchor="middle">
      <circle cx="114" cy="136" r="13" fill="var(--green)"/><path d="M109 147l5 7 5-7z" fill="var(--green)"/><text x="114" y="138">50%</text>
      <circle cx="147" cy="79" r="13" fill="var(--green-dark)"/><path d="M142 90l5 7 5-7z" fill="var(--green-dark)"/><text x="147" y="81">90%</text>
      <circle cx="221" cy="93" r="13" fill="var(--lime)"/><path d="M216 104l5 7 5-7z" fill="var(--lime)"/><text x="221" y="95">80%</text>
    </g>
    <g font-size="6" fill="var(--muted)" text-anchor="middle">
      <text x="99" y="246">2011</text><text x="134" y="246">2012</text><text x="170" y="246">2013</text>
      <text x="206" y="246">2014</text><text x="242" y="246">2015</text><text x="278" y="246">2016</text>
    </g>
  </svg>
  <span class="page-num">3</span>
</section>

<!-- Slide 4: Peru -->
<section class="slide peru">
  <div class="slide__frame"></div>
  <h2 class="slide__title" style="top:19px">Por qué invertir en Perú?</h2>
  <h3 style="left:42px;top:48px">Crecimiento PBI</h3>
  <svg width="368" height="276" viewBox="0 0 368 276">
    <line x1="30" y1="62" x2="115" y2="62" stroke="var(--green)" stroke-width="1"/>
    <line x1="190" y1="76" x2="360" y2="76" stroke="var(--green)" stroke-width="1"/>
  </svg>
  <div role="img" aria-label="Mapa de Sudamérica en gris" style="position:absolute;left:58px;top:62px;width:95px;height:120px;background:radial-gradient(ellipse at 45% 40%,#c9cbcc,#dcdedf 70%,rgba(255,255,255,0) 72%)"></div>

  <div class="country" style="left:14px;top:73px;text-align:right;width:42px"><b>Colombia:</b><br>2017: 2.2%<br>2018: 2.9%</div>
  <div class="flag flag--h" style="left:60px;top:76px"><span style="background:#f5d21f;flex:2"></span><span style="background:#2a55a4"></span><span style="background:#d8252b"></span></div>
  <div class="country country--peru" style="left:14px;top:104px;text-align:right;width:42px"><b>Perú:</b><br>2017: 2.8%<br>2018:4.2%</div>
  <div class="flag" style="left:60px;top:110px"><span style="background:#d8252b"></span><span style="background:#fff"></span><span style="background:#d8252b"></span></div>
  <div class="country" style="left:14px;top:135px;text-align:right;width:42px"><b>Chile:</b><br>2017: 1.6%<br>2018: 2.7%</div>
  <div class="flag flag--h" style="left:60px;top:140px"><span style="background:#fff;border:.3px solid #ccc"></span><span style="background:#d8252b"></span></div>

  <div class="country" style="left:158px;top:70px"><b>México</b><br>2017: 1.8%<br>2018: 2.2%</div>
  <div class="flag" style="left:142px;top:76px"><span style="background:#1a8a4a"></span><span style="background:#fff"></span><span style="background:#d8252b"></span></div>
  <div class="country" style="left:158px;top:102px"><b>Brasil:</b><br>2017: 0.6%<br>2018: 2.5%</div>
  <div class="flag" style="left:142px;top:108px"><span style="background:#2a9a48"></span></div>
  <div class="country" style="left:158px;top:132px"><b>Argentina:</b><br>2017: 2.7%<br>2018: 3.0%</div>
  <div class="flag flag--h" style="left:142px;top:138px"><span style="background:#7eb7e3"></span><span style="background:#fff"></span><span style="background:#7eb7e3"></span></div>

  <h3 style="left:190px;top:48px">Sólidos fundamentos<br>de la economía peruana:</h3>
  <ul class="bullets" style="left:190px;top:84px;width:160px">
    <li>Dentro de las principales economías de LATAM con mayor crecimiento</li>
    <li>Solidez Macroeconómica reconocida internacionalmente</li>
    <li>Clima favorable para la inversión</li>
  </ul>

  <svg width="368" height="276" viewBox="0 0 368 276" font-family="Cabin, sans-serif">
    <text x="184" y="175" font-size="5" font-weight="600" text-anchor="middle" fill="var(--text)">Riesgo País: Spread Soberano</text>
    <text x="184" y="181" font-size="5" font-weight="600" text-anchor="middle" fill="var(--text)">(15-ago-17)</text>
    <g stroke="#e5e7e8" stroke-width=".4">
      <line x1="110" y1="189" x2="262" y2="189"/><line x1="110" y1="196" x2="262" y2="196"/><line x1="110" y1="203" x2="262" y2="203"/>
      <line x1="110" y1="210" x2="262" y2="210"/><line x1="110" y1="217" x2="262" y2="217"/><line x1="110" y1="224" x2="262" y2="224"/>
      <line x1="110" y1="231" x2="262" y2="231"/><line x1="110" y1="238" x2="262" y2="238"/><line x1="110" y1="245" x2="262" y2="245"/>
    </g>
    <g font-size="3.4" fill="var(--muted)" text-anchor="end">
      <text x="108" y="190">500</text><text x="108" y="197">450</text><text x="108" y="204">400</text><text x="108" y="211">350</text>
      <text x="108" y="218">300</text><text x="108" y="225">250</text><text x="108" y="232">200</text><text x="108" y="239">150</text>
      <text x="108" y="246">50</text><text x="108" y="252">0</text>
    </g>
    <g>
      <rect x="121" y="230" width="7" height="21" fill="var(--green)"/>
      <rect x="146" y="189" width="7" height="62" fill="#d4d6d7"/>
      <rect x="171" y="215" width="7" height="36" fill="#d4d6d7"/>
      <rect x="196" y="234" width="7" height="17" fill="#d4d6d7"/>
      <rect x="221" y="223" width="7" height="28" fill="#d4d6d7"/>
      <rect x="246" y="217" width="7" height="34" fill="#d4d6d7"/>
    </g>
    <line x1="110" y1="251" x2="262" y2="251" stroke="#b8bcbe" stroke-width=".5"/>
    <g font-size="3.8" fill="var(--text)" text-anchor="middle">
      <text x="124.5" y="228">154</text><text x="149.5" y="187">447</text><text x="174.5" y="213">263</text>
      <text x="199.5" y="232">124</text><text x="224.5" y="221">201</text><text x="249.5" y="215">244</text>
    </g>
    <g font-size="3.6" fill="var(--muted)" text-anchor="middle">
      <text x="124.5" y="257">Perú</text><text x="149.5" y="257">Argentina</text><text x="174.5" y="257">Brasil</text>
      <text x="199.5" y="257">Chile</text><text x="224.5" y="257">Colombia</text><text x="249.5" y="257">México</text>
    </g>
  </svg>
  <span class="page-num">4</span>
</section>

<!-- Slide 5: group companies -->
<section class="slide companies">
  <div class="slide__frame"></div>
  <h2 class="slide__title" style="top:19px">Empresas del Grupo Inmobiliario</h2>

  <p class="note" style="left:60px;top:47px;width:82px;text-align:right">Lorem ipsum dolor sit amet, consectetur adipisicing elit.</p>
  <p class="note" style="left:218px;top:51px;width:80px">Lorem ipsum dolor sit amet, consectetur.</p>
  <p class="note" style="left:231px;top:107px;width:70px">Lorem ipsum dolor sit amet, consectetur adipisicing.</p>
  <p class="note" style="left:66px;top:121px;width:56px;text-align:right">Lorem ipsum dolor sit amet.</p>
  <p class="note" style="left:58px;top:211px;width:82px;text-align:right">Lorem ipsum dolor sit amet, consectetur adipisicing elit.</p>
  <p class="note" style="left:220px;top:211px;width:86px">Lorem ipsum dolor sit amet, consectetur adipisicing elit, sed do eiusmod tempor incididunt.</p>

  <svg width="368" height="276" viewBox="0 0 368 276" font-family="Cabin, sans-serif">
    <g stroke="#c9cccd" stroke-width=".6" fill="none">
      <path d="M96 68h48l15 15"/><path d="M258 68h-40l-15 15"/>
      <path d="M228 138h50"/><path d="M112 138h-40"/>
      <path d="M96 204h44l13-13"/><path d="M258 204h-40l-13-13"/>
    </g>
    <!-- hexagon ring -->
    <polygon points="149,100 191,100 213,138 191,175 149,175 127,138" fill="none" stroke="var(--green-light)" stroke-width="10" stroke-linejoin="round"/>
    <path d="M149 100L191 100" stroke="var(--lime)" stroke-width="10"/>
    <path d="M213 138L191 175" stroke="var(--teal)" stroke-width="10"/>
    <path d="M191 175L149 175" stroke="var(--lime)" stroke-width="10"/>
    <path d="M191 100L213 138" stroke="var(--green-dark)" stroke-width="10"/>
    <g fill="#fff" stroke="#cfe7c8" stroke-width="1">
      <circle cx="149" cy="100" r="10"/><circle cx="191" cy="100" r="10"/><circle cx="213" cy="138" r="10"/>
      <circle cx="191" cy="175" r="10"/><circle cx="149" cy="175" r="10"/><circle cx="127" cy="138" r="10"/>
    </g>
    <g font-size="8" fill="var(--text)" text-anchor="middle">
      <text x="149" y="103">06</text><text x="191" y="103">01</text><text x="213" y="141">02</text>
      <text x="191" y="178">03</text><text x="149" y="178">04</text><text x="127" y="141">05</text>
    </g>
    <!-- user icon -->
    <circle cx="171" cy="120" r="5" fill="var(--muted)"/>
    <g fill="#fff"><circle cx="169" cy="120" r=".8"/><circle cx="171" cy="120" r=".8"/><circle cx="173" cy="120" r=".8"/></g>
    <circle cx="170" cy="135" r="5.5" fill="var(--muted)"/>
    <path d="M159 155v-6a6 6 0 0 1 6-6h10a6 6 0 0 1 6 6v6z" fill="var(--muted)"/>
  </svg>
  <span class="page-num">5</span>
</section>

</body>
</html>
```